Wedding DJ Services Flyer

Need to make a classy flyer showing and describing different services we offer. I have actual photos from weddings we have done in the past. Stock photos are ok too. Just looking for a front and back, blank space for pricing. Need website and other company info (logo) on the flyer. Front needs to pop with a tagline that screams wedding dj and as soon as a customer sees it, they want to book us. Services we offer are DJ/Emcee, Karaoke, Uplighting, Custom Monogram Projection, Dancing on the Clouds, Custom Love Story Video Slideshow (see my photos, stock photos are ok too).Marlo Vance Entertainment Group, We have been in business since 1998 and provide DJ Event services to all of central and northeastern Pennsylvania. want social media icons on flyer (facebook,instagram,twitter) by website (www.Tqpk.org) and email (Marlo@tqpk.org), phone number 555-283-0146 (call or Text)MORE PHOTOS AVAIL BY REQUEST. Designer should have some knowledge or prior design with this type of business

Target Market(s)

brides and grooms 18-50 yoa

Industry/Entity Type

Entertainment Industry

Colors

Designer to choose colors to be used in the design.

Requirements
Must have
• Photos and descriptions of services we offer

```html
<!DOCTYPE html>
<html lang="en">
<head>
<meta charset="utf-8">
<title>Marlo Vance Entertainment Group – Wedding DJ Flyer</title>
<link href="https://fonts.googleapis.com/css2?family=Great+Vibes&family=Cinzel:wght@400&family=Marcellus+SC&family=Mukta:wght@400;600;700&display=swap" rel="stylesheet">
<style>
  :root{
    --backdrop:#3a2a22;
    --paper:#f6f5f7;
    --plum-deep:#2e0f40;
    --plum:#4a1a63;
    --plum-mid:#6a2a86;
    --magenta:#c21fcf;
    --mauve:#a064b0;
    --gold:#f3c28f;
    --ink:#1d1a20;
    --white:#ffffff;
  }
  *{box-sizing:border-box;margin:0;padding:0}
  html,body{width:1200px;height:900px;overflow:hidden;background:var(--backdrop)}
  body{position:relative;font-family:"Mukta",sans-serif;color:var(--ink)}

  .flyer{position:absolute;background:var(--paper);overflow:hidden;box-shadow:0 4px 14px rgba(0,0,0,.35)}
  .flyer--front{left:57px;top:68px;width:511px;height:717px}
  .flyer--back{left:615px;top:68px;width:517px;height:722px}

  .photo{position:absolute}
  .photo--round{border-radius:50%;border:4px solid var(--white);box-shadow:0 0 0 2px rgba(160,100,176,.45),0 3px 8px rgba(46,15,64,.35)}

  .art{position:absolute;inset:0}

  /* Front */
  .hero-photo{left:0;top:0;width:511px;height:340px;
    background:
      radial-gradient(ellipse 90px 30px at 280px 28px,rgba(255,214,170,.9),transparent 70%),
      radial-gradient(ellipse 260px 70px at 250px 280px,rgba(240,228,246,.95),transparent 75%),
      radial-gradient(ellipse 120px 120px at 260px 170px,rgba(150,110,230,.8),transparent 70%),
      radial-gradient(ellipse 140px 160px at 20px 160px,rgba(220,120,230,.7),transparent 70%),
      radial-gradient(ellipse 140px 160px at 500px 160px,rgba(210,110,210,.7),transparent 70%),
      linear-gradient(180deg,#c7a0bf 0%,#7aa3d8 14%,#4a3a8c 32%,#3a2a62 52%,#9c7ab8 72%,#d8c8e6 100%)}

  .tagline-script{position:absolute;left:222px;top:320px;width:232px;text-align:right;
    font-family:"Great Vibes",cursive;font-size:50px;line-height:1;color:var(--white)}
  .tagline-caps{position:absolute;left:262px;top:374px;width:240px;text-align:right;
    font-family:"Cinzel",serif;font-size:15.5px;letter-spacing:.6px;color:var(--white);text-transform:uppercase}

  .section-tag{position:absolute;background:var(--plum);color:var(--white);
    font-family:"Marcellus SC",serif;font-weight:400;font-size:15px;line-height:22px;padding:0 0 0 22px;
    border-radius:0 12px 12px 0}
  .section-tag--about{left:0;top:520px;width:100px}

  .copy{position:absolute;font-size:9.8px;line-height:12px}
  .copy .line{display:block;white-space:nowrap;text-align:justify;text-align-last:justify}
  .copy .line--end{text-align-last:left}
  .about{left:21px;top:559px;width:284px}
  .about p{margin-bottom:12px}

  .brand{position:absolute;left:322px;top:602px;width:126px;display:flex;align-items:flex-start;gap:6px}
  .brand__dot{width:9px;height:9px;border-radius:50%;background:var(--plum);margin-top:5px;flex:none}
  .brand__name{font-family:"Marcellus SC",serif;font-size:15px;line-height:18px;color:var(--plum-deep)}

  /* Back */
  .couple-photo{left:0;top:0;width:517px;height:240px;
    background:
      radial-gradient(ellipse 150px 130px at 320px 110px,rgba(235,235,235,.85),transparent 70%),
      radial-gradient(ellipse 110px 100px at 230px 190px,rgba(250,250,250,.9),transparent 70%),
      radial-gradient(ellipse 90px 140px at 380px 150px,rgba(25,25,25,.8),transparent 70%),
      radial-gradient(ellipse 80px 120px at 50px 120px,rgba(120,120,120,.7),transparent 70%),
      linear-gradient(180deg,#2a2a2a 0%,#555 50%,#7a7a7a 100%)}
  .section-tag--services{left:19px;top:200px;width:84px;font-size:16px;line-height:24px;padding-left:14px;border-radius:12px}

  .service{position:absolute;left:196px;width:299px}
  .service__title{font-family:"Marcellus SC",serif;font-weight:400;color:var(--plum);font-size:16px;line-height:20px;margin-bottom:2px}
  .service__body{font-size:9.8px;line-height:12.3px}
  .service__body .line{display:block;white-space:nowrap;text-align:justify;text-align-last:justify}
  .service__last{display:flex;align-items:baseline;font-size:9.8px;line-height:14px;white-space:nowrap}
  .service__leader{flex:1;border-bottom:1px dotted var(--ink);margin:0 1px;transform:translateY(-3px)}
  .service__price{font-weight:700;font-size:12.5px;color:var(--plum)}

  .contact-bar{position:absolute;left:0;top:665px;width:517px;height:57px;background:var(--mauve);color:var(--white);font-size:12.5px}
  .contact-bar__item{position:absolute;top:0;height:57px;display:flex;align-items:center;gap:5px}
  .contact-bar__item svg{width:11px;height:11px}
  .social{position:absolute;left:428px;top:0;height:57px;display:flex;align-items:center;gap:10px}
  .social__box{background:var(--white);border-radius:2px}
</style>
</head>
<body>

<section class="flyer flyer--front" aria-label="Flyer front">
  <div class="photo hero-photo" role="img" aria-label="Bride and groom sharing a first dance on a cloud-covered floor in a ballroom lit in purple and blue"></div>

  <svg class="art" width="511" height="717" viewBox="0 0 511 717" aria-hidden="true">
    <defs>
      <linearGradient id="plumSweep" x1="0" y1="0" x2="1" y2="1">
        <stop offset="0" stop-color="#5c2478"/>
        <stop offset="1" stop-color="#2a0c3a"/>
      </linearGradient>
    </defs>
    <path d="M0 290 C120 300 300 262 511 262 L511 717 L500 717 C450 560 280 410 0 380 Z" fill="url(#plumSweep)"/>
    <path d="M0 380 C280 410 450 560 500 717 L0 717 Z" fill="var(--paper)"/>
    <path d="M60 0 C35 120 60 240 130 300" fill="none" stroke="#ffffff" stroke-width="9" opacity=".85"/>
    <path d="M72 0 C60 140 120 270 210 296" fill="none" stroke="#f3c28f" stroke-width="1.2"/>
    <path d="M160 262 C270 240 390 198 511 186" fill="none" stroke="#f3c28f" stroke-width="1.2"/>
    <path d="M215 386 C340 400 460 480 492 717" fill="none" stroke="#f3c28f" stroke-width="1.2"/>
    <path d="M0 400 C260 420 440 560 488 717" fill="none" stroke="#ffffff" stroke-width="6" opacity=".9"/>
  </svg>

  <div class="photo photo--round" style="left:18px;top:292px;width:195px;height:195px;background:radial-gradient(ellipse 50px 30px at 50% 40%,#ffd0f4,transparent 70%),radial-gradient(circle at 50% 45%,#c04ccc,#5a1f78 55%,#1e0a2c)" role="img" aria-label="Reception hall with chandeliers and purple uplighting behind the DJ stage"></div>
  <div class="photo photo--round" style="left:180px;top:409px;width:140px;height:140px;background:radial-gradient(ellipse 50px 20px at 50% 20%,#f2e2fa,transparent 70%),radial-gradient(circle at 50% 55%,#b66ad8,#6a2394 55%,#2a0d3c)" role="img" aria-label="Guests dancing on a purple-lit dance floor"></div>
  <div class="photo photo--round" style="left:316px;top:412px;width:162px;height:162px;background:radial-gradient(circle at 30% 25%,#ffb070,transparent 30%),radial-gradient(ellipse 60px 40px at 60% 80%,#8a7a80,transparent 70%),radial-gradient(circle at 70% 45%,#c8786a,#5b2040 55%,#1c0b18)" role="img" aria-label="Close-up of a hand on a DJ mixing console"></div>

  <div class="tagline-script">Dance to the</div>
  <div class="tagline-caps">Rhythm of your heart</div>

  <h2 class="section-tag section-tag--about">About Us</h2>
  <div class="copy about">
    <p><span class="line line--end">We are in business since 1998.</span></p>
    <p>
      <span class="line">Four friends formed ‘Harbor Light Productions’, which was later</span>
      <span class="line">sold and is still successfully operating today! Around 2003 we</span>
      <span class="line">ventured into the Karaoke world and for many years operated</span>
      <span class="line line--end">under ‘Velvet Mic Karaoke’.</span>
    </p>
    <p>
      <span class="line">We are a DJ/KJ/Trivia Service based in Northeast Pennsylvania.</span>
      <span class="line">We offer a large library of Music &amp; Karaoke and provide DJ</span>
      <span class="line">Event services to all of central and northeastern Pennsylvania.</span>
    </p>
  </div>

  <div class="brand">
    <span class="brand__dot"></span>
    <span class="brand__name">Marlo Vance Entertainment Group</span>
  </div>
</section>

<section class="flyer flyer--back" aria-label="Flyer back">
  <div class="photo couple-photo" role="img" aria-label="Black and white photo of a bride and groom embracing during their first dance, guests behind them"></div>

  <svg class="art" width="517" height="722" viewBox="0 0 517 722" aria-hidden="true">
    <path d="M0 150 C120 160 230 228 320 228 C410 228 470 182 517 168 L517 722 L0 722 Z" fill="#c21fcf"/>
    <path d="M0 163 C120 172 230 238 320 238 C410 238 470 195 517 184 L517 722 L0 722 Z" fill="#4a1a63"/>
    <path d="M0 176 C120 186 230 248 320 248 C410 248 470 215 517 206 L517 722 L0 722 Z" fill="#f3c28f"/>
    <path d="M0 180 C120 190 230 252 320 252 C410 252 470 219 517 210 L517 722 L0 722 Z" fill="var(--paper)"/>
  </svg>

  <h2 class="section-tag section-tag--services">Services</h2>

  <div class="photo photo--round" style="left:20px;top:238px;width:112px;height:112px;background:radial-gradient(circle at 70% 30%,#e0c8f0,transparent 35%),radial-gradient(circle at 45% 50%,#8a5aa8,#4a2a7a 55%,#1a0a30)" role="img" aria-label="DJ performing at a wedding reception"></div>
  <div class="photo photo--round" style="left:70px;top:310px;width:112px;height:112px;background:radial-gradient(ellipse 40px 30px at 60% 75%,#f4eeee,transparent 70%),radial-gradient(circle at 50% 40%,#c89a80,#6a4030 55%,#2a1810)" role="img" aria-label="Bride and groom singing karaoke on stage"></div>
  <div class="photo photo--round" style="left:18px;top:390px;width:112px;height:112px;background:radial-gradient(ellipse 50px 20px at 50% 70%,#e6ddf6,transparent 70%),radial-gradient(circle at 50% 35%,#9a70f0,#5a38b8 55%,#241458)" role="img" aria-label="Banquet room washed in purple uplighting"></div>
  <div class="photo photo--round" style="left:73px;top:460px;width:112px;height:112px;background:radial-gradient(ellipse 35px 25px at 50% 35%,#f6f0d0,transparent 70%),radial-gradient(circle at 50% 50%,#b8a040,#7a6a1c 55%,#2e2810)" role="img" aria-label="Custom monogram projected on a wall above a wedding cake"></div>
  <div class="photo photo--round" style="left:18px;top:544px;width:112px;height:112px;background:radial-gradient(ellipse 60px 30px at 50% 75%,#f6f2fc,transparent 75%),radial-gradient(circle at 50% 40%,#9a7ad8,#5a3aa8 50%,#2a1060)" role="img" aria-label="Couple dancing on a low cloud of white fog"></div>

  <article class="service" style="top:238px">
    <h3 class="service__title">DJ/Emcee</h3>
    <div class="service__body">
      <span class="line">Our all-inclusive style DJ package includes all the essentials</span>
      <span class="line">needed to throw one exciting wedding reception. We focus our</span>
      <span class="line">efforts in on providing peace of mind, coordination</span>
    </div>
    <div class="service__last"><span>and hospitality</span><span class="service__leader"></span><span class="service__price">$00.00</span></div>
  </article>
  <article class="service" style="top:318px">
    <h3 class="service__title">Karaoke</h3>
    <div class="service__body">
      <span class="line">We ventured into the Karaoke world around 2003 and for many</span>
    </div>
    <div class="service__last"><span>years operated under ‘Velvet Mic Karaoke’</span><span class="service__leader"></span><span class="service__price">$00.00</span></div>
  </article>
  <article class="service" style="top:373px">
    <h3 class="service__title">Uplighting</h3>
    <div class="service__body">
      <span class="line">Uplighting instantly transforms a room from drab to fab and with</span>
      <span class="line">more than 50,000 colors to choose from. Uplighting can enhance</span>
      <span class="line">your natural coloring, showcase your dress and highlight your</span>
    </div>
    <div class="service__last"><span>flowers for photographs</span><span class="service__leader"></span><span class="service__price">$00.00</span></div>
  </article>
  <article class="service" style="top:452px">
    <h3 class="service__title">Custom Monogram Projection</h3>
    <div class="service__body">
      <span class="line">Add your initials to your wedding decor with an elegant custom</span>
    </div>
    <div class="service__last"><span>monogram light display</span><span class="service__leader"></span><span class="service__price">$00.00</span></div>
  </article>
  <article class="service" style="top:507px">
    <h3 class="service__title">Dancing on the Clouds</h3>
    <div class="service__body">
      <span class="line">Dancing on a Cloud or Dancing on Clouds is a “special effect” that</span>
      <span class="line">produces a thick white cloud of smoke resembling, well, a cloud!</span>
      <span class="line">During Weddings, Dancing on a Cloud is used during a first</span>
    </div>
    <div class="service__last"><span>dance</span><span class="service__leader"></span><span class="service__price">$00.00</span></div>
  </article>
  <article class="service" style="top:586px">
    <h3 class="service__title">Custom Love Story Video Slideshow</h3>
    <div class="service__body">
      <span class="line">Want to tell and share you love story? A picture is worth a</span>
      <span class="line">thousand words means and a photo slideshow is a great way to</span>
    </div>
    <div class="service__last"><span>do that</span><span class="service__leader"></span><span class="service__price">$00.00</span></div>
  </article>

  <footer class="contact-bar">
    <span class="contact-bar__item" style="left:33px">
      <svg viewBox="0 0 12 12" aria-hidden="true"><circle cx="6" cy="6" r="5" fill="none" stroke="#fff" stroke-width="1.2"/><ellipse cx="6" cy="6" rx="2.2" ry="5" fill="none" stroke="#fff" stroke-width="1"/><line x1="1" y1="6" x2="11" y2="6" stroke="#fff" stroke-width="1"/></svg>
      www.Tqpk.org
    </span>
    <span class="contact-bar__item" style="left:158px">
      <svg viewBox="0 0 12 12" aria-hidden="true"><rect x="1" y="2.5" width="10" height="7" fill="#fff"/><path d="M1 2.5 L6 6.5 L11 2.5" fill="none" stroke="#a064b0" stroke-width="1"/></svg>
      Marlo@tqpk.org
    </span>
    <span class="contact-bar__item" style="left:301px">
      <svg viewBox="0 0 12 12" aria-hidden="true"><path d="M3 1 L5 3.5 L4 5 C4.8 6.6 5.6 7.4 7 8 L8.5 7 L11 9 L9.5 11 C5 10.5 1.5 7 1 2.5 Z" fill="#fff"/></svg>
      555-283-0146
    </span>
    <span class="social" aria-label="Social media">
      <span class="social__box" style="width:7px;height:12px"></span>
      <span class="social__box" style="width:14px;height:12px"></span>
      <span class="social__box" style="width:12px;height:12px"></span>
    </span>
  </footer>
</section>

</body>
</html>
```